Linewise Trade Journal Adverts

We need an advertisement design for our company 'Brindle Harbor' www.brindleharbor.example
Brindle Harbor is a telecommunication business that develop three different service. Cloud, Voice and Connectivity.
We are wanting to put an advertisement into Linewise Trade and would like the design, design that reflects our current brand and captures individual attention.
This advertisement needs to look professional and eye catching.
3 different advertisements are needed and I would like them to all be different yet link together in design so they can be recognised as Brindle Harbor.
I have attached our logo below, along with the three advertisements.
Target Market(s)
Direct Reseller customers
Industry/Entity Type
Telecommunications
Requirements
Must have
- My project must follow our current branding that is on our website

```html
<!DOCTYPE html>
<html lang="en">
<head>
<meta charset="utf-8">
<title>Brindle Harbor – Linewise Trade Adverts</title>
<link rel="stylesheet" href="https://fonts.googleapis.com/css2?family=Fira+Sans:wght@600&family=Montserrat:wght@300;400;500;600;700;800&display=swap">
<style>
:root{
  --stage:#95a8a6;
  --magenta:#e412c8;
  --magenta-deep:#a80a93;
  --ink:#333536;
  --text:#2f3132;
  --paper-top:#ffffff;
  --paper-bottom:#e8e9e9;
  --icon-disc:#c9cccd;
}
*{box-sizing:border-box;margin:0;padding:0}
html,body{width:1200px;height:1200px;overflow:hidden}
body{background:var(--stage);position:relative;font-family:"Montserrat",sans-serif;color:var(--text)}
.service-label{position:absolute;width:400px;text-align:center;font-family:"Fira Sans",sans-serif;font-weight:600;font-size:40px;color:#fff;line-height:1}
.ad{position:absolute;width:496px;height:382px;overflow:hidden;background:radial-gradient(ellipse at 60% 35%,var(--paper-top) 30%,var(--paper-bottom) 100%)}
.ad > *{position:absolute}
.brand{left:30px;top:42px;display:flex;align-items:center;gap:8px;font-size:19px;font-weight:500;color:var(--ink);letter-spacing:.3px;white-space:nowrap}
.brand-dot{width:16px;height:16px;border-radius:50%;background:var(--magenta)}
.headline{font-weight:400;font-size:24px;line-height:.98;color:var(--text);white-space:nowrap}
.headline .amount{font-weight:800;font-size:34px;color:var(--magenta)}
.kicker{color:var(--magenta);font-weight:700;line-height:1.05;white-space:nowrap}
.pink-box{background:var(--magenta);color:#fff;display:flex;align-items:center;padding-left:9px;white-space:nowrap}
.pink-box .small{font-weight:400;font-size:16px;margin-right:6px;margin-top:5px}
.pink-box .big{font-weight:800;font-size:27px}
.pink-note{color:var(--magenta);font-size:13px;line-height:1.25;white-space:nowrap}
.fine{font-size:9.5px;line-height:1.2;color:var(--text);white-space:nowrap}
.placeholder{border-radius:6px}
.footer-art{left:0;top:0;width:496px;height:382px}
.cta{left:270px;top:308px;height:27px;display:flex;align-items:center;color:#fff;font-size:10px;font-weight:500}
.contacts{left:262px;top:353px;display:flex;align-items:center;gap:10px;color:#fff;font-size:6px;white-space:nowrap}
.contacts span{display:flex;align-items:center;gap:5px}
.benefit{width:70px;text-align:center;font-size:9px;font-weight:700;line-height:1.2}
.benefit svg{display:block;margin:0 auto 5px}
.bullets{list-style:none;font-size:8.3px;font-weight:700;line-height:10.5px}
.bullets li::before{content:"• ";color:var(--magenta)}
</style>
</head>
<body>

<svg width="0" height="0" style="position:absolute">
  <defs>
    <symbol id="footer" viewBox="0 0 496 382">
      <path d="M0 363 H190 C215 363 222 323 256 323 H496 V382 H0 Z" fill="#333536"/>
      <path d="M246 312 C248 306 262 306 266 310 V320 C258 316 250 316 246 318 Z" fill="#a80a93"/>
      <rect x="262" y="308" width="234" height="27" fill="#e412c8"/>
    </symbol>
    <symbol id="phone" viewBox="0 0 10 10">
      <path d="M2 1 L4 1 L4.6 3 L3.4 3.8 C4 5.2 4.8 6 6.2 6.6 L7 5.4 L9 6 L9 8 C9 8.6 8.6 9 8 9 C4.2 9 1 5.8 1 2 C1 1.4 1.4 1 2 1Z" fill="#fff"/>
    </symbol>
    <symbol id="globe" viewBox="0 0 10 10">
      <circle cx="5" cy="5" r="4" fill="none" stroke="#fff" stroke-width=".8"/>
      <ellipse cx="5" cy="5" rx="1.8" ry="4" fill="none" stroke="#fff" stroke-width=".7"/>
      <path d="M1 5 H9 M1.6 3 H8.4 M1.6 7 H8.4" stroke="#fff" stroke-width=".6"/>
    </symbol>
  </defs>
</svg>

<!-- Cloud -->
<div class="service-label" style="left:116px;top:126px">Cloud</div>
<section class="ad ad-cloud" style="left:70px;top:189px">
  <div class="brand"><span class="brand-dot"></span>Brindle Harbor</div>
  <div class="headline" style="left:238px;top:17px">What about <span class="amount">£2m</span><br>additional revenue</div>
  <div class="pink-box" style="left:236px;top:81px;width:238px;height:41px"><span class="small">in only</span><span class="big">12 months?</span></div>
  <div style="left:238px;top:130px;font-size:13px;white-space:nowrap">There’s nothing standard about that</div>
  <div class="kicker" style="left:238px;top:170px;font-size:13px">Most channel partners offer these<br>benefits as standard:</div>
  <div class="benefit" style="left:235px;top:216px">
    <svg width="40" height="40" viewBox="0 0 40 40"><circle cx="20" cy="20" r="19" fill="var(--icon-disc)"/><circle cx="22" cy="14" r="5" fill="none" stroke="#333" stroke-width="1.4"/><path d="M13 30 C13 23 31 23 31 30" fill="none" stroke="#333" stroke-width="1.4"/><circle cx="13" cy="24" r="3.5" fill="none" stroke="#333" stroke-width="1.4"/></svg>
    Account management</div>
  <div class="benefit" style="left:308px;top:216px">
    <svg width="40" height="40" viewBox="0 0 40 40"><circle cx="20" cy="20" r="19" fill="var(--icon-disc)"/><rect x="13" y="18" width="14" height="12" rx="1.5" fill="#333"/><path d="M15.5 18 V14 A4.5 4.5 0 0 1 24.5 14 V18" fill="none" stroke="#333" stroke-width="2"/><circle cx="20" cy="23.5" r="1.6" fill="#c9cccd"/></svg>
    A secure portal</div>
  <div class="benefit" style="left:379px;top:216px;width:80px">
    <svg width="40" height="40" viewBox="0 0 40 40"><circle cx="20" cy="20" r="19" fill="var(--icon-disc)"/><circle cx="15" cy="15" r="4" fill="none" stroke="#333" stroke-width="1.6"/><circle cx="25" cy="15" r="3" fill="none" stroke="#333" stroke-width="1.6"/><circle cx="23" cy="26" r="4.5" fill="none" stroke="#333" stroke-width="1.6"/></svg>
    An automated billing engine</div>
  <div class="placeholder" role="img" aria-label="Illustration of a cloud linked to a ring of laptops" style="left:24px;top:91px;width:206px;height:172px;background:radial-gradient(ellipse at 50% 30%,#bfe6f5 0%,#dfe9ee 45%,rgba(230,232,233,0) 75%)"></div>
  <div class="pink-note" style="left:28px;top:290px">We’ll supercharge your<br>business with secure network</div>
  <div class="fine" style="left:28px;top:322px">and storage solutions that enable your<br>clients – and you – to thrive.</div>
  <svg class="footer-art"><use href="#footer"/></svg>
  <div class="cta">Talk to us about your partner potential</div>
  <div class="contacts"><span><svg width="8" height="8"><use href="#phone"/></svg>0300 555 0187</span><span><svg width="8" height="8"><use href="#globe"/></svg>www.brindleharbor.example/make-a-connection</span></div>
</section>

<!-- Voice -->
<div class="service-label" style="left:680px;top:126px">Voice</div>
<section class="ad ad-voice" style="left:635px;top:189px">
  <div class="brand" style="top:38px"><span class="brand-dot"></span>Brindle Harbor</div>
  <div class="kicker" style="left:231px;top:36px;font-size:15px">Struggling to Stand Out in the<br><span style="font-size:24px">Crowded IT Space?</span></div>
  <div class="headline" style="left:231px;top:91px">We’re talking <span class="amount">£2m</span><br>additional revenue</div>
  <div class="pink-box" style="left:235px;top:162px;width:238px;height:41px"><span class="small">in only</span><span class="big">12 months?</span></div>
  <div class="pink-note" style="right:23px;top:222px;text-align:right">We’ll deliver leads to<br>your sales team</div>
  <div class="fine" style="right:23px;top:258px;text-align:right">free of charge, using our AI-driven<br>marketing platform</div>
  <div class="placeholder" role="img" aria-label="Photograph of a smiling support agent wearing a headset" style="left:41px;top:83px;width:148px;height:280px;border-radius:70px 70px 0 0;background:linear-gradient(180deg,#7a4a36 0%,#d9b6a0 30%,#f3f3f3 55%,#e4e4e4 100%)"></div>
  <svg class="footer-art"><use href="#footer"/></svg>
  <div class="cta">Ready to talk?</div>
  <div class="contacts"><span><svg width="8" height="8"><use href="#phone"/></svg>0300 555 0187</span><span><svg width="8" height="8"><use href="#globe"/></svg>www.brindleharbor.example/make-a-connection</span></div>
</section>

<!-- Connectivity -->
<div class="service-label" style="left:392px;top:646px">Connectivity</div>
<section class="ad ad-connectivity" style="left:334px;top:708px">
  <div class="brand" style="top:38px"><span class="brand-dot"></span>Brindle Harbor</div>
  <div class="kicker" style="left:246px;top:26px;font-size:18px">We’re Here to Make Our<br><span style="font-size:27px">Partners Money</span></div>
  <div class="headline" style="left:246px;top:86px">How’s &nbsp;<span class="amount">£2m</span><br>additional revenue</div>
  <div class="pink-box" style="left:238px;top:146px;width:238px;height:40px;padding-left:12px"><span class="small" style="font-size:13px">in</span><span class="big" style="font-size:21px">12 months sound?</span></div>
  <div style="right:20px;top:199px;width:240px;text-align:right;font-size:5.5px;line-height:1.4">Scattered image of all the benefits of Brindle Harbor (a bit like a word cloud) with the main point front and centre, e.g.</div>
  <ul class="bullets" style="left:245px;top:233px"><li>Cloud-first</li><li>Multichannel</li><li>Secure portal</li><li>GDPR-compliant</li><li>24/7 support</li></ul>
  <ul class="bullets" style="left:366px;top:233px"><li>Corvane partner</li><li>Award-winning</li><li>Dedicated account<br>&nbsp;&nbsp;management</li><li>Lead generation FOC</li><li>AI capabilities</li></ul>
  <div class="placeholder" role="img" aria-label="Illustration of a circuit tree branching into phone and device icons" style="left:18px;top:84px;width:188px;height:280px;background:radial-gradient(ellipse at 50% 38%,#2a5bd8 0%,#4aa9ea 35%,#bde6ec 60%,rgba(232,233,233,0) 80%)"></div>
  <svg class="footer-art"><use href="#footer"/></svg>
  <div class="cta">Talk to us about your partner potential</div>
  <div class="contacts"><span><svg width="8" height="8"><use href="#phone"/></svg>0300 555 0187</span><span><svg width="8" height="8"><use href="#globe"/></svg>www.brindleharbor.example/make-a-connection</span></div>
</section>

</body>
</html>
```